Zielgruppe
Wir sind ein kleines Restaurant in den schweizer Bergen. Unsere sonnige Terrasse mit bester Aussicht auf die umliegende Berglandschaft, läd zum verweilen und geniessen ein. Unser Publikum sind vor allem mehr oder weniger sportliche Schweizer jeden Alters, die auf ihrem Weg zu/von den umliegenden Wanderungen bei uns vorbei kommen, aber auch ältere Semester die nicht mehr so gut zu Fuß sind und deshalb auf der Terrasse verweilen. Auch Touristen kommen vorbei, wir sind für die aber mehr ein Geheimtipp. Am späten Nachmittag kommen ein paar Anwohner vorbei auf ein Feierabendgetränk und am Wochenende haben wir öfters die selben 'Einheimischen' hier für ein Mittagessen. Unser Angebot ist eher traditionell gehalten, aber wir wollen Gerichte anbieten die nicht auf jeder Hütte zu finden sind. Ich komme aus Tirol, meine Mitarbeiterin hier aus der Schweiz - deshalb haben wir einen Mix aus beiden Nationen auf den Tellern. Wir streben einen moderneren/coolen Stil an, der zu uns 'jungen Mädels' passt, der aber noch stark von Tradition und der Bergwelt geprägt ist. Unser Stübli ist sehr urig, aus dunkelm Holz gebaut und mit weissen Schaffellen und Kissen gemütlich gemacht. Die Einrichtung haben wir in den Farben weiss, dunkelrot und beige-brauntönen gehalten.
Aufgabenstellung
bitte nichts kitschiges oder zu buntes.
Die Masse 25x25 oder 26x26 gefallen uns am besten.
Der 'Hinweis' mit der MwSt und CHF sowie Kartenzahlung sollte bitte als kleine Fusszeile auf jeder Seite (ausser Titelseite und zweite Seite) sein

```html
<!DOCTYPE html>
<html lang="de">
<head>
<meta charset="utf-8">
<title>Getränkekarte – Es Schnäpsli</title>
<link rel="stylesheet" href="https://fonts.googleapis.com/css2?family=Kaushan+Script&family=Zilla+Slab:ital,wght@0,400;0,600;0,700;1,400;1,700&display=swap">
<style>
  :root {
    --backdrop: #e4e1d4;
    --wood-dark: #4a4644;
    --wood-light: #c08a57;
    --panel: #ede2d4;
    --ink: #3a3430;
    --accent: #b9844f;
    --rule: #c9a074;
    --paper-white: #ffffff;
  }
  * { margin: 0; padding: 0; box-sizing: border-box; }
  html, body { width: 1200px; height: 884px; overflow: hidden; background: var(--backdrop); }
  .spread {
    position: absolute; left: 40px; top: 162px;
    width: 1120px; height: 560px; display: flex;
  }
  .page { position: relative; width: 560px; height: 560px; }
  .page--left { background: linear-gradient(90deg, #403d3b, var(--wood-dark) 40%, #555150 75%, #3f3c3a); }
  .page--right { background: linear-gradient(90deg, #c48e5b, var(--wood-light) 30%, #b98250 60%, #c58f5c); }
  .page-title {
    position: absolute; left: 62px; top: 238px;
    transform: translate(-50%, -50%) rotate(-90deg);
    font-family: "Kaushan Script", cursive; font-size: 46px; line-height: 1;
    font-weight: 400; color: var(--paper-white); white-space: nowrap;
  }
  .menu-panel {
    position: absolute; left: 104px; top: 48px; width: 356px; height: 468px;
    background: var(--panel);
  }
  .section-title {
    position: absolute; left: 0; top: 28px; width: 100%;
    text-align: center; padding-left: 0; transform: translateX(0);
    font-family: "Kaushan Script", cursive; font-size: 22px; font-weight: 400;
    line-height: 30px; color: var(--accent);
    margin-left: 0;
  }
  .section-title span { display: inline-block; transform: translateX(0); margin-left: 0; position: relative; left: 0; }
  .drink-list {
    position: absolute; left: 0; top: 66px; width: 100%; list-style: none;
  }
  .drink {
    display: grid; grid-template-columns: 217px 11px auto;
    align-items: baseline; height: 22.3px; white-space: nowrap;
    font-family: "Zilla Slab", serif; color: var(--ink);
  }
  .drink__main { grid-column: 1; text-align: right; }
  .drink__name { font-weight: 700; font-size: 12.5px; }
  .drink__detail { font-style: italic; font-size: 10.5px; margin-left: 3px; }
  .drink__price {
    grid-column: 3; font-weight: 700; font-style: italic;
    font-size: 11.5px; color: var(--accent);
  }
  .illustration-rules { position: absolute; left: 0; top: 0; }
  .illustration {
    position: absolute; left: 146px; top: 260px; width: 77px; height: 173px;
    background: linear-gradient(180deg, #e8d3ba, #ddbb94);
    border-radius: 6px;
  }
  .price-note {
    position: absolute; left: 0; width: 564px; top: 535px; text-align: center;
    font-family: "Zilla Slab", serif; font-weight: 700; font-size: 7.6px; line-height: 10px;
    color: var(--paper-white); white-space: nowrap;
  }
</style>
</head>
<body>
<main class="spread">
  <section class="page page--left">
    <h1 class="page-title">U was gits z'Trüche?</h1>
    <div class="menu-panel">
      <h2 class="section-title">Es Schnäpsli</h2>
      <ul class="drink-list">
        <li class="drink"><span class="drink__main"><span class="drink__name">Genepy</span><span class="drink__detail">40 %, 2cl</span></span><span class="drink__price">5,00</span></li>
        <li class="drink"><span class="drink__main"><span class="drink__name">44er hausgemacht</span><span class="drink__detail">37,5 %, 2cl</span></span><span class="drink__price">5,00</span></li>
        <li class="drink"><span class="drink__main"><span class="drink__name">Alpenkräuter</span><span class="drink__detail">29 %, 4cl</span></span><span class="drink__price">6,50</span></li>
        <li class="drink"><span class="drink__main"><span class="drink__name">Marillen</span><span class="drink__detail">34 %, 2cl</span></span><span class="drink__price">5,00</span></li>
        <li class="drink"><span class="drink__main"><span class="drink__name">Grappa</span><span class="drink__detail">41 %, 2cl</span></span><span class="drink__price">6,00</span></li>
        <li class="drink"><span class="drink__main"><span class="drink__name">Vieille Prune</span><span class="drink__detail">40 %, 2cl</span></span><span class="drink__price">6,00</span></li>
      </ul>
      <svg class="illustration-rules" width="356" height="468" aria-hidden="true">
        <line x1="100" y1="414" x2="145" y2="414" stroke="var(--rule)" stroke-width="1"/>
        <line x1="221" y1="414" x2="264" y2="414" stroke="var(--rule)" stroke-width="1"/>
      </svg>
      <div class="illustration" role="img" aria-label="Strichzeichnung einer Grappaflasche mit Stielglas"></div>
    </div>
    <p class="price-note">Hinweis: alle Preise verstehen sich inkl. MwSt. und in CHF<br>Kartenzahlungen akzeptieren wir ab einem Mindestbetrag von 20,00</p>
  </section>
  <section class="page page--right" aria-label="Rückseite in Holzoptik"></section>
</main>
</body>
</html>
```